"Harborline Inc." Needs a Logo Design and Business Card

The name of the company is "Harborline Inc."
Our Business decription, which should appear on the front of the Business Card along with the logo and business name is:
"Boutique Global Procurement and Management Services"
We offer the following SERVICES that should be listed on the back of the Business Card :
"Consultants"
"Management"
"Business Research & Development"
"Sourcing Agent"
"Distributors"
We would like to see designs that use the colors
burnt orange and,
stainless steel
Business card designs should be innovatively modern and contemporary
Telephone number and email address should be on the back of the card
The name of the firm is "Harborline Inc.
Steel

```html
<!DOCTYPE html>
<html lang="en">
<head>
<meta charset="utf-8">
<title>Harborline Inc. — Business Card</title>
<link rel="stylesheet" href="https://fonts.googleapis.com/css2?family=Quicksand:wght@300;400&display=swap">
<style>
  :root {
    --page: #fef7cf;
    --card: #353535;
    --card-deep: #262626;
    --band: #272727;
    --steel-light: #cfcfcf;
    --orange: #ff6633;
    --ampersand: #6a3a2a;
    --shadow: rgba(60, 50, 20, 0.55);
  }
  html, body {
    margin: 0;
    padding: 0;
    width: 1200px;
    height: 699px;
    overflow: hidden;
    background: var(--page);
    font-family: "Quicksand", sans-serif;
    font-weight: 300;
  }
  .stage { position: relative; width: 1200px; height: 699px; }

  .card {
    position: absolute;
    background: var(--card);
    overflow: hidden;
    box-shadow: 6px 7px 6px var(--shadow);
  }
  .card svg.decor { position: absolute; left: 0; top: 0; }

  /* Back of card */
  .card-back { left: 207px; top: 93px; width: 301px; height: 525px; }
  .card-back .company {
    position: absolute; right: 9px; top: 97px;
    margin: 0; font-size: 24px; font-weight: 300;
    color: var(--steel-light); line-height: 1;
  }
  .services {
    position: absolute; right: 11px; top: 137px;
    margin: 0; padding: 0; list-style: none;
    text-align: right; color: var(--orange);
    font-size: 19px; line-height: 21px;
  }
  .services li { margin-bottom: 21px; }
  .contact-band {
    position: absolute; left: 0; top: 444px; width: 100%; height: 43px;
    background: var(--band);
    color: var(--orange); text-align: center;
    font-size: 15px; font-weight: 400; letter-spacing: 0.6px; line-height: 21px;
    padding-top: 2px; box-sizing: border-box;
  }

  /* Front of card */
  .card-front { left: 581px; top: 273px; width: 524px; height: 300px; }
  .name-band {
    position: absolute; left: 0; top: 98px; width: 100%; height: 31px;
    background: rgba(18, 18, 18, 0.72);
  }
  .card-front .company {
    position: absolute; right: 8px; top: 102px;
    margin: 0; font-size: 24px; font-weight: 300;
    color: var(--steel-light); line-height: 1;
  }
  .brand-dot {
    position: absolute; left: 320px; top: 49px;
    width: 30px; height: 30px; border-radius: 50%;
    background: var(--steel-light);
  }
  .ampersand {
    position: absolute; left: 316px; top: 226px;
    font-size: 72px; line-height: 1; color: var(--ampersand);
  }
  .tagline {
    position: absolute; right: 9px; top: 250px; margin: 0;
    text-align: right; color: var(--orange);
    font-size: 17px; line-height: 21px;
  }
</style>
</head>
<body>
<main class="stage">

  <section class="card card-back" aria-label="Back of business card">
    <svg class="decor" width="301" height="525" viewBox="0 0 301 525" aria-hidden="true">
      <circle cx="142" cy="145" r="113" fill="var(--card-deep)"/>
      <circle cx="65" cy="264" r="67" fill="rgba(255,255,255,0.16)"/>
    </svg>
    <h2 class="company">Harborline Inc.</h2>
    <ul class="services">
      <li>Consultants</li>
      <li>Management</li>
      <li>Research<br>&amp; Development</li>
      <li>Sourcing Agents</li>
      <li>Distributors</li>
    </ul>
    <div class="contact-band">
      1-888-555-0172<br>contact-us@harborlineintl.com
    </div>
  </section>

  <section class="card card-front" aria-label="Front of business card">
    <svg class="decor" width="524" height="300" viewBox="0 0 524 300" aria-hidden="true">
      <circle cx="87" cy="169" r="78" fill="var(--orange)"/>
      <circle cx="197" cy="235" r="44" fill="rgba(255,255,255,0.15)"/>
      <circle cx="441" cy="115" r="115" fill="rgba(255,255,255,0.15)"/>
    </svg>
    <div class="name-band"></div>
    <span class="brand-dot" aria-hidden="true"></span>
    <h1 class="company">Harborline Inc.</h1>
    <span class="ampersand" aria-hidden="true">&amp;</span>
    <p class="tagline">Boutique Global Procurement<br>Management Services</p>
  </section>

</main>
</body>
</html>
```